business card template & company stationery
for Blue Pine Device Wizard - Computer Support
business card template & company stationery -
Creative Brief
Bright & Fun-filled
Dale Harwick
Service Manager
47 E. Birch Ave. (Rt. 58) Norton, MA 02519
dale@bluepinedevicewizard.com
www.BluePineDeviceWizard.com
I will upload the logo info shortly. The phone number is the most important contact info for us.
On the back of the card I was planning to have either a solid blue or orange background with our logo centered in all white, but I'm open to other ideas. The white on blue and orange versions are included with the logos

```html
<!DOCTYPE html>
<html lang="en">
<head>
<meta charset="utf-8">
<title>Blue Pine Device Wizard – Stationery Set</title>
<link href="https://fonts.googleapis.com/css2?family=Open+Sans:wght@400;600;700&display=swap" rel="stylesheet">
<style>
  :root{
    --backdrop:#2d2d2e;
    --backdrop-dark:#232324;
    --brand-blue:#3b7dc9;
    --brand-orange:#f4821f;
    --ink-black:#111;
    --paper:#fdfdfd;
    --paper-shade:#e9ebee;
    --muted:#8a8f96;
    --label:#6d6f72;
  }
  *{box-sizing:border-box;margin:0;padding:0}
  html,body{width:1200px;height:312px;overflow:hidden}
  body{
    font-family:"Open Sans",Arial,sans-serif;
    background:radial-gradient(ellipse at center,var(--backdrop) 0%,var(--backdrop-dark) 100%);
    position:relative;
  }
  .item{position:absolute}
  .label{
    position:absolute;font-size:4px;color:var(--label);
    letter-spacing:.2px;white-space:nowrap;transform:translateX(-50%);
  }
  .brand{font-weight:700;white-space:nowrap;line-height:1}
  .brand small{display:block;font-weight:600;font-size:.62em;margin-top:1px}

  /* business cards */
  .card{width:74px;height:40px;box-shadow:0 1px 3px rgba(0,0,0,.5)}
  .card--front{background:var(--paper);padding:5px}
  .card--front .brand{color:var(--brand-blue);font-size:5.5px}
  .card--front .contact{margin-top:4px;font-size:2.4px;line-height:1.35;color:#444}
  .card--front .contact strong{color:var(--brand-blue);font-size:3px}
  .card--back{display:flex;align-items:center;justify-content:center}
  .card--back .brand{color:#fff;font-size:6px;text-align:center}
  .card--blue{background:var(--brand-blue)}
  .card--orange{background:var(--brand-orange)}

  /* letterheads */
  .letterhead{width:210px;height:274px;background:var(--paper);box-shadow:0 1px 4px rgba(0,0,0,.5)}
  .letterhead__band{height:5px;background:var(--brand-blue)}
  .letterhead__brand{position:absolute;top:12px;left:62px;color:var(--brand-blue);font-size:8px}
  .letterhead__footer{
    position:absolute;bottom:8px;left:0;right:0;text-align:center;
    font-size:3px;color:var(--muted)
  }

  /* DL envelopes */
  .envelope{width:240px;height:112px;background:var(--paper);box-shadow:0 1px 4px rgba(0,0,0,.5)}
  .envelope__band{height:5px;background:var(--brand-blue)}
  .envelope__brand{position:absolute;top:12px;left:12px;color:var(--brand-blue);font-size:7px}
  .envelope__return{position:absolute;top:30px;left:12px;font-size:3px;color:var(--muted);line-height:1.4}

  /* envelope backs */
  .env-back{width:254px;height:60px;background:var(--paper-shade);box-shadow:0 1px 3px rgba(0,0,0,.5);overflow:hidden}
  .env-back svg{position:absolute;inset:0}
  .env-back .brand{position:absolute;left:50%;top:24px;transform:translateX(-50%);font-size:6px;color:#fff}
  .env-back--white .brand{color:var(--brand-blue)}
</style>
</head>
<body>

  <!-- business cards -->
  <div class="item card card--front" style="left:24px;top:110px">
    <div class="brand">Blue Pine Device Wizard<small>Computer Support</small></div>
    <div class="contact">
      <strong>Dale Harwick</strong><br>Service Manager<br>
      47 E. Birch Ave. (Rt. 58) Norton, MA 02519<br>
      dale@bluepinedevicewizard.com<br>www.BluePineDeviceWizard.com
    </div>
  </div>
  <div class="item card card--front" style="left:102px;top:110px">
    <div class="brand">Blue Pine Device Wizard<small>Computer Support</small></div>
  </div>
  <div class="item card card--back card--orange" style="left:24px;top:160px">
    <div class="brand">Blue Pine Device Wizard<small>Computer Support</small></div>
  </div>
  <div class="item card card--back card--blue" style="left:102px;top:160px">
    <div class="brand">Blue Pine Device Wizard<small>Computer Support</small></div>
  </div>
  <div class="label" style="left:101px;top:206px">Business Cards</div>

  <!-- letterheads -->
  <div class="item letterhead" style="left:212px;top:19px">
    <div class="letterhead__band"></div>
    <div class="brand letterhead__brand">Blue Pine Device Wizard<small>Computer Support</small></div>
    <div class="letterhead__footer">47 E. Birch Ave. (Rt. 58) Norton, MA 02519 · dale@bluepinedevicewizard.com · www.BluePineDeviceWizard.com</div>
  </div>
  <div class="label" style="left:317px;top:298px">Letterhead Front</div>

  <div class="item letterhead" style="left:444px;top:19px">
    <div class="letterhead__band"></div>
    <div class="brand letterhead__brand">Blue Pine Device Wizard<small>Computer Support</small></div>
    <div class="letterhead__footer">47 E. Birch Ave. (Rt. 58) Norton, MA 02519 · www.BluePineDeviceWizard.com</div>
  </div>
  <div class="label" style="left:549px;top:298px">Letterhead Second</div>

  <!-- DL envelopes -->
  <div class="item envelope" style="left:667px;top:24px">
    <div class="envelope__band"></div>
    <div class="brand envelope__brand">Blue Pine Device Wizard<small>Computer Support</small></div>
    <div class="envelope__return">47 E. Birch Ave. (Rt. 58)<br>Norton, MA 02519</div>
  </div>
  <div class="label" style="left:787px;top:142px">DL Envelope</div>

  <div class="item envelope" style="left:667px;top:156px;height:104px">
    <svg width="240" height="104" viewBox="0 0 240 104" aria-hidden="true">
      <polyline points="0,0 120,52 240,0" fill="none" stroke="#d6d9de" stroke-width="1"/>
    </svg>
  </div>
  <div class="label" style="left:787px;top:264px">DL Envelope Back</div>

  <!-- envelope backs, four colourways -->
  <div class="item env-back" style="left:922px;top:19px">
    <svg width="254" height="60" viewBox="0 0 254 60" aria-hidden="true">
      <path d="M0,0 H254 V12 Q127,58 0,12 Z" fill="var(--brand-blue)"/>
    </svg>
    <div class="brand">Blue Pine Device Wizard</div>
  </div>
  <div class="item env-back" style="left:922px;top:85px">
    <svg width="254" height="60" viewBox="0 0 254 60" aria-hidden="true">
      <path d="M0,0 H254 V12 Q127,58 0,12 Z" fill="var(--ink-black)"/>
    </svg>
    <div class="brand">Blue Pine Device Wizard</div>
  </div>
  <div class="item env-back" style="left:922px;top:151px">
    <svg width="254" height="60" viewBox="0 0 254 60" aria-hidden="true">
      <path d="M0,0 H254 V12 Q127,58 0,12 Z" fill="var(--brand-orange)"/>
    </svg>
    <div class="brand">Blue Pine Device Wizard</div>
  </div>
  <div class="item env-back env-back--white" style="left:922px;top:217px">
    <svg width="254" height="60" viewBox="0 0 254 60" aria-hidden="true">
      <path d="M0,0 H254 V12 Q127,58 0,12 Z" fill="var(--paper)" stroke="#d6d9de" stroke-width=".8"/>
    </svg>
    <div class="brand">Blue Pine Device Wizard</div>
  </div>
  <div class="label" style="left:1049px;top:282px">Envelope Backs</div>

</body>
</html>
```